Custom Framing Shop Tallpine Framing Studio

I want an eye catching graphic that will be used a s business sign on a busy road. The sign MUST communicate the type of business it is clearly to vehicles traveling at 40 mph. This is a custom picture framing business and the sign will be hanging and be approximately 32" X 48". The business name is Tallpine Framing Studio; Custom framing: by appointment and should include a whole or partial image of a picture frame as a visual que. I've included inspiration idea's, color pallets and styles that I like and a current business card for inspiration. I like the crimson font style shadowing and background colors of the attached Olans pizzeria sign. I'd prefer crimson letters. Custom Framing is the message to communicate, followed by phone number and business name. I like the idea of a shield shape with a banner since it would more eye catching, Once again the Tallpine image and name is less important than communicating what the business does. I like Crimson, grey, gold, black but am open to new ideas . I like the idea of a shield with a banner more than a rectangle, but am open to idea's

Target Market(s)

My target market is local homeowners ($700k+) who want a relationship with their framer and are willing to pay for a customized experience compared to a craft store experience. I have more female clients then men.

Industry/Entity Type

Picture Framing Art

Other font styles liked:
• Look at the attached image of a custom pizzeria sign, its kid of a custom car pinstripe font style. Script and decorative may be difficult to read while driving by but add to the elegance.

Colors

Designer to choose colors to be used in the design.

Requirements
Must have
• Clearly communicate what the business does "Custom framing" preferably with a picture frame and words
Nice to have
• incorporate a Tallpine into the graphic
Should not have
• A Tallpine image doesn't communicate what the business does to a vehicle traveling at 40 mph by the sign

```html
<!DOCTYPE html>
<html lang="en">
<head>
<meta charset="utf-8">
<title>Tallpine Framing Studio – Hanging Sign</title>
<link href="https://fonts.googleapis.com/css2?family=Alfa+Slab+One&family=Rye&family=Libre+Caslon+Text&family=Oswald:wght@600&display=swap" rel="stylesheet">
<style>
  :root {
    --crimson: #a3191f;
    --crimson-dark: #7d1116;
    --cream: #f3ebdc;
    --black: #141414;
    --gold: #c99a3c;
    --backdrop: #e7e4de;
  }
  html, body {
    margin: 0;
    padding: 0;
    width: 800px;
    height: 1200px;
    overflow: hidden;
    background: var(--backdrop);
  }
  .canvas {
    position: relative;
    width: 800px;
    height: 1200px;
  }
  .sign-shape {
    position: absolute;
    left: 40px;
    top: 20px;
    width: 720px;
    height: 1160px;
  }
  .sign-content {
    position: absolute;
    left: 60px;
    top: 40px;
    width: 680px;
    height: 1120px;
  }
  .emblem {
    position: absolute;
    left: 250px;
    top: 22px;
    width: 180px;
    height: 215px;
    border-radius: 14px;
    background: linear-gradient(160deg, var(--crimson) 0%, var(--crimson-dark) 70%, var(--black) 100%);
  }
  .business-name {
    position: absolute;
    left: 0;
    top: 232px;
    width: 680px;
    margin: 0;
    text-align: center;
    font-family: "Alfa Slab One", serif;
    font-weight: 400;
    font-size: 104px;
    line-height: 1;
    color: var(--crimson);
    transform: scaleY(1.3);
    transform-origin: center top;
    white-space: nowrap;
  }
  .studio-line {
    position: absolute;
    left: 0;
    top: 398px;
    width: 680px;
    display: flex;
    align-items: center;
    justify-content: center;
    gap: 18px;
    font-family: "Libre Caslon Text", serif;
    font-size: 38px;
    line-height: 1;
    color: var(--black);
    letter-spacing: 0.5px;
  }
  .studio-line .rule {
    width: 52px;
    height: 2px;
    background: var(--gold);
  }
  .service {
    position: absolute;
    left: 48px;
    top: 478px;
    width: 600px;
    margin: 0;
    text-align: center;
    font-family: "Rye", serif;
    font-weight: 400;
    font-size: 112px;
    line-height: 132px;
    color: var(--cream);
    white-space: nowrap;
  }
  .appointment {
    position: absolute;
    left: 40px;
    top: 780px;
    width: 610px;
    height: 105px;
    display: flex;
    align-items: center;
    justify-content: center;
    gap: 18px;
    font-family: "Libre Caslon Text", serif;
    font-size: 38px;
    color: var(--cream);
    letter-spacing: 0.5px;
  }
  .appointment .rule {
    width: 60px;
    height: 2px;
    background: var(--gold);
  }
  .phone {
    position: absolute;
    left: 0;
    top: 928px;
    width: 680px;
    text-align: center;
    font-family: "Oswald", sans-serif;
    font-weight: 600;
    font-size: 84px;
    line-height: 1;
    color: var(--black);
    letter-spacing: 1px;
  }
</style>
</head>
<body>
<main class="canvas">
  <svg class="sign-shape" viewBox="-20 -20 720 1160" aria-hidden="true">
    <path class="sign-board"
      d="M0,80 H110 Q130,80 150,55 Q340,-20 530,55 Q550,80 570,80 H680 V900 C655,900 640,915 640,940 V1000 Q340,1180 40,1000 V940 C40,915 25,900 0,900 Z"
      fill="var(--cream)" stroke="var(--crimson)" stroke-width="26" stroke-linejoin="round"/>
    <path class="sign-inner-line"
      d="M14,93 H114 Q138,93 160,68 Q340,0 520,68 Q542,93 566,93 H666 V887 C645,887 627,905 627,935 V992 Q340,1160 53,992 V935 C53,905 35,887 14,887 Z"
      fill="none" stroke="var(--crimson-dark)" stroke-width="1.5"/>

    <path class="service-panel"
      d="M62,465 H634 Q634,479 648,479 V757 Q634,757 634,771 H62 Q62,757 48,757 V479 Q62,479 62,465 Z"
      fill="var(--black)" stroke="var(--gold)" stroke-width="3"/>
    <rect class="panel-accent" x="318" y="457" width="44" height="16" rx="8" fill="var(--gold)" role="img" aria-label="Small gold flourish"/>
    <rect class="panel-accent" x="318" y="763" width="44" height="16" rx="8" fill="var(--gold)" role="img" aria-label="Small gold flourish"/>

    <path class="appointment-banner"
      d="M54,780 H636 Q636,794 650,794 V871 Q636,871 636,885 H54 Q54,871 40,871 V794 Q54,794 54,780 Z"
      fill="var(--crimson)" stroke="var(--black)" stroke-width="4"/>
    <rect x="50" y="788" width="590" height="89" fill="none" stroke="var(--gold)" stroke-width="1"/>

    <line class="divider" x1="80" y1="914" x2="600" y2="914" stroke="var(--gold)" stroke-width="2"/>
    <rect class="divider-accent" x="315" y="907" width="50" height="14" rx="7" fill="var(--gold)" role="img" aria-label="Small gold flourish"/>
    <line class="divider" x1="120" y1="1046" x2="560" y2="1046" stroke="var(--gold)" stroke-width="2"/>
    <rect class="divider-accent" x="315" y="1039" width="50" height="14" rx="7" fill="var(--gold)" role="img" aria-label="Small gold flourish"/>
  </svg>

  <div class="sign-content">
    <div class="emblem" role="img" aria-label="Crimson and black bird emblem illustration"></div>
    <h1 class="business-name">TALLPINE</h1>
    <div class="studio-line"><span class="rule"></span>FRAMING STUDIO<span class="rule"></span></div>
    <h2 class="service">CUSTOM<br>FRAMING</h2>
    <div class="appointment"><span class="rule"></span>BY APPOINTMENT<span class="rule"></span></div>
    <div class="phone">(360) 555-0147</div>
  </div>
</main>
</body>
</html>
```